Natural healthcare clinic needs stationery and business card design

We have had a logo developed by Pixel Harbor and are now looking at utilising it for a new business concept. The concept is a natural healthcare clinic that hosts a number of small businesses. The individual practitioners may want to utilise the host business stationery to provide a consistent message to clients.

I am looking for a stationery design - letterhead, DL brochure template and business card that uses our logo. The business name 'Bright Meadows' is all about getting rhythm back into your life so you can be fit and healthy. The stationery design should reflect this.

There are a couple of requirements for the business card, it needs to be double-sided with black and white back. There should be lines to write appointment times on. The cards may need to be custom named on the front for example Carys Dunmore, Remedial Therapist and Aromatherapist. Therefore if a template can be provided so we can customise this information using MS Publisher, it would be appreciated.

The DL brochure template needs to be A4 folded to DL. I am looking for a consistent brand message that can be utilised to produce our own clinic brochures.

The natural healthcare clinic will host the following types of businesses - remedial massage, pregnancy massage, oncology massage, aromatherapy, acupuncture - as a bit of a guide.

Target Market(s)

25-45 year old male and females who work full time.

Industry/Entity Type

Healthcare

Requirements
Must have
• Use the logo I have already.

```html
<!DOCTYPE html>
<html lang="en">
<head>
<meta charset="utf-8">
<title>Bright Meadows – Business Card</title>
<link href="https://fonts.googleapis.com/css2?family=Open+Sans:wght@300;400;600&display=swap" rel="stylesheet">
<style>
  :root{
    --backdrop:#e9e6e1;
    --card-black:#0c0c0c;
    --card-white:#ffffff;
    --leaf-green:#8fb03a;
    --text-light:#e8e8e8;
    --text-dark:#4a4a4a;
    --rule-grey:#9a9a9a;
    --dot-orange:#f08a24;
    --dot-blue:#4a6fc4;
    --dot-yellow:#e3dc2a;
  }
  *{box-sizing:border-box;margin:0;padding:0}
  html,body{width:1200px;height:1024px;overflow:hidden}
  body{
    background:var(--backdrop);
    font-family:"Open Sans",Arial,sans-serif;
    position:relative;
  }
  .card{
    position:absolute;
    left:200px;
    width:800px;
    height:457px;
    box-shadow:0 6px 18px rgba(0,0,0,.18);
  }
  .card--front{top:34px;background:var(--card-black);color:var(--text-light)}
  .card--back{top:533px;background:var(--card-white);color:var(--text-dark)}

  /* front */
  .brand{
    position:absolute;left:70px;top:150px;
    display:flex;align-items:center;gap:14px;
  }
  .brand__dot{width:22px;height:22px;border-radius:50%;background:var(--leaf-green)}
  .brand__name{
    font-weight:300;font-size:44px;color:var(--leaf-green);letter-spacing:-.5px;
  }
  .divider{
    position:absolute;left:448px;top:118px;width:2px;height:150px;
    background:linear-gradient(to bottom,rgba(143,176,58,0),var(--leaf-green) 50%,rgba(143,176,58,0));
  }
  .contacts{
    position:absolute;left:482px;top:124px;list-style:none;
  }
  .contacts li{
    display:flex;align-items:center;gap:12px;
    font-size:20px;line-height:34px;font-weight:400;color:var(--text-light);
  }
  .contacts svg{width:16px;height:16px;flex:none}
  .practitioner{position:absolute;left:70px;top:322px}
  .practitioner__name{font-size:24px;font-weight:400;color:var(--leaf-green);line-height:30px}
  .practitioner__role{font-size:20px;font-weight:400;color:var(--text-light);line-height:26px}

  /* back */
  .watermark{
    position:absolute;left:60px;top:40px;width:420px;height:380px;border-radius:50%;
    background:radial-gradient(ellipse at center,rgba(246,214,190,.45),rgba(255,255,255,0) 70%);
  }
  .appointment__title{
    position:absolute;left:0;right:0;top:38px;text-align:center;
    font-size:28px;font-weight:400;letter-spacing:1px;color:#333;
  }
  .appointment__fields{position:absolute;left:70px;right:70px;top:100px}
  .field{display:flex;align-items:flex-end;height:50px}
  .field__label{font-size:17px;color:#555;width:66px}
  .field__line{flex:1;border-bottom:1px solid var(--rule-grey);margin-bottom:5px}
  .services{
    position:absolute;left:0;right:0;top:330px;text-align:center;
    font-size:17px;line-height:26px;color:#444;
  }
  .services__dot{
    display:inline-block;width:11px;height:11px;border-radius:50%;
    margin:0 6px;vertical-align:middle;
  }
  .services__dot--orange{background:var(--dot-orange)}
  .services__dot--blue{background:var(--dot-blue)}
  .services__dot--yellow{background:var(--dot-yellow)}
  .services__web{color:var(--leaf-green);font-size:16px}
</style>
</head>
<body>

<section class="card card--front" aria-label="Business card front">
  <div class="brand">
    <span class="brand__dot"></span>
    <span class="brand__name">Bright Meadows</span>
  </div>
  <div class="divider"></div>
  <ul class="contacts">
    <li>
      <svg viewBox="0 0 16 16" fill="var(--leaf-green)"><path d="M3.5 1.5l2.5 0 1 3.5-1.6 1.2a8 8 0 0 0 4.4 4.4L11 9l3.5 1v2.5c0 .8-.7 1.5-1.5 1.5C7 14 2 9 2 3c0-.8.7-1.5 1.5-1.5z"/></svg>
      415-2036-7184
    </li>
    <li>
      <svg viewBox="0 0 16 16" fill="none" stroke="var(--leaf-green)" stroke-width="1.6"><rect x="4" y="1" width="8" height="14" rx="1.5"/><line x1="7" y1="12.5" x2="9" y2="12.5"/></svg>
      415-6621-0937
    </li>
    <li>
      <svg viewBox="0 0 16 16" fill="none" stroke="var(--leaf-green)" stroke-width="1.6"><rect x="1.5" y="3.5" width="13" height="9" rx="1"/><path d="M1.5 4l6.5 5 6.5-5"/></svg>
      care@brightmeadows.com
    </li>
    <li>
      <svg viewBox="0 0 16 16" fill="none" stroke="var(--leaf-green)" stroke-width="1.4"><circle cx="8" cy="8" r="6.5"/><ellipse cx="8" cy="8" rx="3" ry="6.5"/><line x1="1.5" y1="8" x2="14.5" y2="8"/></svg>
      www.brightmeadows.com
    </li>
  </ul>
  <div class="practitioner">
    <p class="practitioner__name">Carys Dunmore</p>
    <p class="practitioner__role">Remedial Therapist<br>and Aromatherapist</p>
  </div>
</section>

<section class="card card--back" aria-label="Business card back – appointment card">
  <div class="watermark" role="img" aria-label="Faint pastel brand decoration"></div>
  <h1 class="appointment__title">APPOINTMENT</h1>
  <div class="appointment__fields">
    <div class="field"><span class="field__label">FOR:</span><span class="field__line"></span></div>
    <div class="field"><span class="field__label">DAY:</span><span class="field__line"></span></div>
    <div class="field"><span class="field__label">DATE:</span><span class="field__line"></span></div>
    <div class="field"><span class="field__label">TIME:</span><span class="field__line"></span></div>
  </div>
  <p class="services">
    Remedial massage<span class="services__dot services__dot--orange"></span>Pregnancy massage<span class="services__dot services__dot--yellow"></span>Oncology massage<br>
    Aromatherapy<span class="services__dot services__dot--blue"></span>Acupuncture<br>
    <span class="services__web">www.brightmeadows.com</span>
  </p>
</section>

</body>
</html>
```